Elegant Financial Planning Business Card

Clearpath Wealth Advisory Pty Ltd requires an elegant business card that communicates simplicity, elegance and trust.
Attached card example of 'Varnoth' is very close to what I am looking for. Looking for black and white card.
Update 24/1/16: The attached Varnoth card is almost exactly what I am looking for. Although it is possible that alternative layouts may interest me, it is considerably more likely that I will proceed with a virtual clone of the "Varnoth' example.
Industry/Entity Type
Financial Planning
Contact Information for Business Card
In black font...
Front Details are (layout as per Dana Varnoth card picture):
Line1 - Name: Oliver Marsh
Line 2 - Company: Clearpath Wealth Advisory Pty Ltd
Line 3 - Address: Harbourview Plaza 3, Level 17, 58 Lomond Avenue, Bondi Junction NSW
Line 4
- Phone: 136 712
- Email: advice@cpwa-example.com.au
- Site: www.cpwa-example.com.au
Back details
1/ logo in position and dimensions as per attached layout
2. Bottom left (in smaller writing).
- Authorised Representative No. 517946
- Clearpath Wealth Advisory is a corporate authorised representative of Tarquay7 Capital Services Pty Ltd
- ABN 47 318 602 154
- AFSL No. 608139

```html
<!DOCTYPE html>
<html lang="en">
<head>
<meta charset="utf-8">
<title>Clearpath Wealth Advisory – Business Card</title>
<link href="https://fonts.googleapis.com/css2?family=Tinos:ital,wght@0,400;1,400&display=swap" rel="stylesheet">
<style>
  :root {
    --backdrop: #2e2825;
    --card-black: #111111;
    --card-edge: #1c1c1c;
    --ink-light: #e8e8e8;
    --ink-muted: #bdbdbd;
    --gloss-mark: #3a3a3a;
    --fine-print: #4a4a4a;
  }
  * { margin: 0; padding: 0; box-sizing: border-box; }
  html, body {
    width: 1200px;
    height: 716px;
    overflow: hidden;
    background: var(--backdrop);
    font-family: "Tinos", "Times New Roman", serif;
  }
  .canvas {
    position: relative;
    width: 1200px;
    height: 716px;
  }
  .card {
    position: absolute;
    top: 208px;
    width: 500px;
    height: 300px;
    background: var(--card-black);
    border: 1px solid var(--card-edge);
    border-radius: 4px;
    box-shadow: 0 6px 18px rgba(0, 0, 0, 0.45);
  }
  .card--brand { left: 70px; }
  .card--contact { left: 630px; }

  /* Brand side */
  .brand-mark {
    position: absolute;
    left: 0;
    right: 0;
    top: 128px;
    display: flex;
    align-items: center;
    justify-content: center;
    gap: 14px;
  }
  .brand-mark__square {
    width: 18px;
    height: 18px;
    background: var(--gloss-mark);
  }
  .brand-mark__name {
    font-size: 26px;
    font-weight: 400;
    color: var(--gloss-mark);
    letter-spacing: 0.5px;
  }
  .compliance {
    position: absolute;
    left: 28px;
    right: 28px;
    bottom: 22px;
    font-size: 8px;
    line-height: 1.45;
    color: var(--fine-print);
    list-style: none;
  }

  /* Contact side */
  .contact {
    position: absolute;
    inset: 0;
    padding: 34px 40px;
    color: var(--ink-light);
  }
  .contact__name {
    font-size: 22px;
    font-weight: 400;
    line-height: 1.1;
  }
  .contact__role {
    margin-top: 4px;
    font-size: 11px;
    font-style: italic;
    color: var(--ink-muted);
  }
  .contact__company {
    position: absolute;
    left: 40px;
    top: 176px;
    font-size: 18px;
    font-weight: 400;
  }
  .contact__address,
  .contact__lines {
    position: absolute;
    left: 40px;
    font-size: 12px;
    color: var(--ink-light);
    white-space: nowrap;
  }
  .contact__address { top: 208px; }
  .contact__lines { top: 226px; }
  .contact__sep { margin: 0 6px; color: var(--ink-muted); }
</style>
</head>
<body>
<main class="canvas">
  <section class="card card--brand" aria-label="Business card, brand side">
    <div class="brand-mark">
      <span class="brand-mark__square"></span>
      <span class="brand-mark__name">Clearpath Wealth Advisory</span>
    </div>
    <ul class="compliance">
      <li>Authorised Representative No. 517946</li>
      <li>Clearpath Wealth Advisory is a corporate authorised representative of Tarquay7 Capital Services Pty Ltd</li>
      <li>ABN 47 318 602 154</li>
      <li>AFSL No. 608139</li>
    </ul>
  </section>

  <section class="card card--contact" aria-label="Business card, contact side">
    <div class="contact">
      <h1 class="contact__name">Oliver Marsh</h1>
      <p class="contact__role">Managing Director</p>
      <p class="contact__company">Clearpath Wealth Advisory Pty Ltd</p>
      <p class="contact__address">Harbourview Plaza 3, Level 17, 58 Lomond Avenue, Bondi Junction NSW</p>
      <p class="contact__lines">136 712<span class="contact__sep">|</span>advice@cpwa-example.com.au<span class="contact__sep">|</span>www.cpwa-example.com.au</p>
    </div>
  </section>
</main>
</body>
</html>
```